Letterhead design for Sleep Consulting Business

I'm looking for a new letterhead (heading/footer) design for my Sleep Consulting Business, I work with families to help their children improve their sleep.

The heading/footer will used in Microsoft Word Only-to be used for all of my documents such as writing Sleep Plans. I need to utilize as much working space in the document as possible. This will NOT be printed out on paper- it will only be used for heading/footer on microsoft word, then emailed to clients, who may print it at home.

My brand colors:
Dark Blue Hex: 1F2A42
Lighter Blueish Hex: 90BEC9
You're welcome to check out my website for inspiration- it is freshly created with other colors as well, and I love the outcome. www.quietharborsleep.example

Target Market(s)

Tired parents

Font styles to use
Script
Other font styles liked:
• Great Vibe, Lato or Just Another Hand are all used currently for my brand. Open to other options.

Requirements
Must have
• The letterhead (heading/footer) MUST be kept narrow (height-wise), so I have plenty of space on my document, while including important information.

It should look professional on screen, and when printed.

Must include my business name OR logo (Quiet Harbor Sleep Consulting), and my email address. Tessa@quietharborsleep.example

Website is optional, not required, just if you need to fill in a spot: www.quietharborsleep.example

```html
<!DOCTYPE html>
<html lang="en">
<head>
<meta charset="utf-8">
<title>Quiet Harbor Sleep Consulting — Letterhead</title>
<link rel="stylesheet" href="https://fonts.googleapis.com/css2?family=Lato:wght@400&family=Montserrat:wght@600&display=swap">
<style>
  :root {
    --navy: #1f2a42;
    --mist: #90bec9;
    --paper: #ffffff;
    --shade: #ececec;
  }
  html, body {
    margin: 0;
    padding: 0;
    overflow: hidden;
    background: var(--paper);
  }
  .letterhead {
    position: relative;
    width: 848px;
    height: 1200px;
    overflow: hidden;
    background: var(--paper);
  }
  .backdrop {
    position: absolute;
    inset: 0;
  }
  .brand {
    position: absolute;
    left: 238px;
    top: 46px;
    display: flex;
    align-items: center;
    gap: 18px;
  }
  .brand-dot {
    width: 92px;
    height: 92px;
    border-radius: 50%;
    background: var(--mist);
  }
  .brand-name {
    font-family: "Lato", sans-serif;
    font-weight: 400;
    color: var(--navy);
    line-height: 1;
  }
  .brand-name .line-main {
    display: block;
    font-size: 40px;
    letter-spacing: 0.5px;
  }
  .brand-name .line-sub {
    display: block;
    margin-top: 12px;
    font-size: 13px;
    letter-spacing: 5.2px;
    padding-left: 2px;
  }
  .header-rule {
    position: absolute;
    left: 109px;
    top: 159px;
    width: 631px;
    height: 2px;
    background: linear-gradient(to right,
      var(--navy) 0, var(--navy) 242px,
      var(--mist) 242px, var(--mist) 388px,
      var(--navy) 388px);
  }
  .contact {
    position: absolute;
    top: 1112px;
    display: flex;
    align-items: center;
    gap: 10px;
    font-family: "Montserrat", sans-serif;
    font-weight: 600;
    font-size: 12px;
    letter-spacing: 3.3px;
    color: var(--navy);
    white-space: nowrap;
  }
  .contact-email { left: 55px; }
  .contact-web { left: 447px; }
  .contact-icon {
    width: 24px;
    height: 24px;
    flex: none;
  }
  .contact-divider {
    position: absolute;
    left: 432px;
    top: 1108px;
    width: 1.5px;
    height: 32px;
    background: var(--mist);
  }
  .footer-band {
    position: absolute;
    left: 0;
    bottom: 0;
    width: 848px;
    height: 41px;
  }
</style>
</head>
<body>
<main class="letterhead">
  <svg class="backdrop" width="848" height="1200" viewBox="0 0 848 1200" aria-hidden="true">
    <defs>
      <linearGradient id="fadeDown" x1="0" y1="0" x2="0" y2="1">
        <stop offset="0" stop-color="#e6e6e6" stop-opacity="0.9"/>
        <stop offset="1" stop-color="#ffffff" stop-opacity="0"/>
      </linearGradient>
      <linearGradient id="fadeUp" x1="0" y1="1" x2="0" y2="0">
        <stop offset="0" stop-color="#e4e4e4" stop-opacity="0.9"/>
        <stop offset="1" stop-color="#ffffff" stop-opacity="0"/>
      </linearGradient>
    </defs>
    <polygon points="0,0 310,0 470,300 120,340 0,140" fill="url(#fadeDown)"/>
    <polygon points="80,0 150,0 330,330 250,340" fill="url(#fadeDown)"/>
    <polygon points="415,0 640,0 800,300 600,330" fill="url(#fadeDown)"/>
    <polygon points="580,0 700,0 848,260 848,330" fill="url(#fadeDown)"/>
    <polygon points="40,820 250,780 470,1160 120,1160" fill="url(#fadeUp)"/>
    <polygon points="150,900 220,880 380,1160 290,1160" fill="url(#fadeUp)"/>
    <polygon points="560,860 760,820 848,960 848,1160 720,1160" fill="url(#fadeUp)"/>
    <polygon points="640,980 700,960 820,1160 760,1160" fill="url(#fadeUp)"/>
  </svg>

  <header class="brand">
    <span class="brand-dot" aria-hidden="true"></span>
    <span class="brand-name">
      <span class="line-main">Quiet Harbor</span>
      <span class="line-sub">SLEEP CONSULTING</span>
    </span>
  </header>
  <div class="header-rule"></div>

  <footer>
    <div class="contact contact-email">
      <svg class="contact-icon" viewBox="0 0 24 24" aria-hidden="true">
        <circle cx="12" cy="12" r="12" fill="var(--mist)"/>
        <rect x="6" y="8" width="12" height="8.5" rx="0.8" fill="#fff"/>
        <polyline points="6.4,8.5 12,13 17.6,8.5" fill="none" stroke="var(--mist)" stroke-width="1"/>
      </svg>
      <span>tessa@quietharborsleep.example</span>
    </div>
    <div class="contact-divider"></div>
    <div class="contact contact-web">
      <svg class="contact-icon" viewBox="0 0 24 24" aria-hidden="true">
        <circle cx="12" cy="12" r="12" fill="var(--mist)"/>
        <g fill="none" stroke="#fff" stroke-width="1">
          <circle cx="12" cy="12" r="6.5"/>
          <ellipse cx="12" cy="12" rx="3" ry="6.5"/>
          <line x1="5.5" y1="12" x2="18.5" y2="12"/>
          <line x1="12" y1="5.5" x2="12" y2="18.5"/>
          <line x1="6.5" y1="9" x2="17.5" y2="9"/>
          <line x1="6.5" y1="15" x2="17.5" y2="15"/>
        </g>
      </svg>
      <span>www.quietharborsleep.example</span>
    </div>
    <svg class="footer-band" viewBox="0 0 848 41" aria-hidden="true">
      <rect x="0" y="0" width="848" height="41" fill="var(--mist)"/>
      <polygon points="0,0 440,0 465,41 0,41" fill="var(--navy)"/>
    </svg>
  </footer>
</main>
</body>
</html>
```